Call Center In Need of Website Design

We are a call center that provides inbound and outbound calling & marketing services for eCommerce store. We would like to see a fun, creative, playful design that is simple.

Here are some sample design sites we like;
- https://www.velmorink.com/
- https://tonquel.io/
- https://www.brasklode.com/live-chat-software/
- https://www.quillarbe.com/

Here are some competitor sites;
- https://www.dorvenlinkage.com/
- https://www.helpwaldrix.com/

I have attached website content for your use.
Updates

Target Market(s)

eCommerce

Coding

Coded - Design and coding required

Number of Pages Required

5+ page

Font styles to use
Sans Serif

Colors

Designer to choose colors to be used in the design.

Requirements
Must have
• Must have designs for the following 5 separate pages;
• 1. Home (landing)
• - This will be were the design style really needs to show.
• - Just needs to touch on key services
• - CTA
• 2. About Us
• - Basic page for about me paragraph
• 3. Services
• - List of services with icons
• - Click on service type to expand details or hover over service icon to view popup bubble with details about that service
• 4. Pricing
• - Option to bundle 1(one) digital service plan and 1(one) call center service plan
• - Bundling adds 10% monthly discount to over all price
• - Customer does NOT have to bundle
• - FAQ
• 5. Contact Us
• - Include a capture form (name, company name, email, phone, message)
• - Contact info
• - Business hours
• When customer purchases their desired plan, then they are taken to a page where they must schedule a call with an account rep.
Nice to have
• home page animations
Should not have
• All information on Home/Landing page.

```html
<!DOCTYPE html>
<html lang="en">
<head>
<meta charset="utf-8">
<title>Lumora — Call Center Services for eCommerce</title>
<link rel="stylesheet" href="https://fonts.googleapis.com/css2?family=Raleway:wght@400;500;600&family=Open+Sans:wght@400;600;700&display=swap">
<style>
:root{
  --green:#5cbd9a;
  --green-dark:#4fae8b;
  --ink:#333638;
  --text:#4a4d50;
  --muted:#8a8d90;
  --line:#cfd2d4;
  --white:#ffffff;
  --footer:#25272a;
  --footer-text:#e4e5e6;
}
*{box-sizing:border-box;margin:0;padding:0}
html,body{width:1200px;height:2359px;overflow:hidden}
body{position:relative;background:var(--white);font-family:"Open Sans",Arial,sans-serif;color:var(--text)}
.icons{position:absolute;width:0;height:0}

/* header */
.site-header{position:absolute;top:0;left:0;width:1200px;height:114px;z-index:3}
.brand{position:absolute;left:98px;top:30px;display:flex;align-items:center;gap:16px}
.brand-mark{width:46px;height:46px;border:3px solid var(--green);border-radius:50%}
.brand-name{font-family:"Raleway",Arial,sans-serif;font-weight:500;font-size:34px;letter-spacing:7px;color:var(--ink)}
.main-nav{position:absolute;left:424px;top:45px;display:flex;gap:28px;align-items:center}
.main-nav a{font-family:"Raleway",Arial,sans-serif;font-weight:600;font-size:16px;color:var(--ink);text-decoration:none}
.main-nav a.is-active{color:var(--green)}
.nav-search{width:16px;height:16px;margin-left:4px}
.btn-signup{position:absolute;left:996px;top:34px;width:106px;height:46px;border-radius:23px;background:var(--green);color:var(--white);font-family:"Open Sans",Arial,sans-serif;font-weight:700;font-size:15px;display:flex;align-items:center;justify-content:center;gap:6px;text-decoration:none}
.btn-signup svg{width:14px;height:14px}

/* hero */
.hero{position:absolute;top:0;left:0;width:1200px;height:613px;overflow:hidden}
.hero-photo{position:absolute;inset:0;background:
  radial-gradient(ellipse 260px 300px at 860px 330px,#d9cfc4 0%,rgba(217,207,196,0) 100%),
  linear-gradient(90deg,#f7eebf 0%,#f5f1e0 18%,#f1f1ef 38%,#ececeb 60%,#e2e3e4 80%,#ebecec 100%)}
.hero-title{position:absolute;left:97px;top:180px;font-family:"Open Sans",Arial,sans-serif;font-weight:600;font-size:68px;letter-spacing:1px;color:var(--ink)}
.hero-lead{position:absolute;left:98px;top:283px;width:500px;font-size:18px;line-height:33px;color:var(--ink)}
.signup-form{position:absolute;left:98px;top:377px;display:flex;height:54px}
.signup-input{width:339px;height:54px;border:1px solid #9a9c9e;background:var(--white);display:flex;align-items:center;gap:8px;padding-left:18px;font-size:15px;color:var(--muted)}
.signup-input svg{width:15px;height:12px}
.signup-btn{width:145px;height:54px;background:var(--green);color:var(--white);font-weight:700;font-size:16px;display:flex;align-items:center;justify-content:center;letter-spacing:.3px}

/* welcome */
.welcome{position:absolute;top:712px;left:0;width:1200px;text-align:center}
.section-title{font-family:"Raleway",Arial,sans-serif;font-weight:500;color:var(--ink)}
.welcome .section-title{font-size:37px;letter-spacing:.5px}
.welcome-text{width:830px;margin:40px auto 0;font-size:14.5px;line-height:28.5px;color:var(--text)}

/* service blocks */
.service{position:absolute}
.service .section-title{font-size:33px}
.service-lead{font-size:14px;line-height:28px;color:var(--text);margin-top:20px}
.check-list{list-style:none;margin-top:34px}
.check-list li{display:flex;align-items:center;gap:14px;height:36px;font-size:14.5px;color:var(--text)}
.check-list svg{width:15px;height:15px;flex:none}
.btn-cta{display:flex;align-items:center;justify-content:center;width:155px;height:57px;border-radius:29px;background:var(--green);color:var(--white);font-weight:700;font-size:16px;text-decoration:none}

.service-digital{left:96px;top:976px;width:520px}
.service-digital .btn-cta{margin-top:51px}
.art-digital{position:absolute;left:610px;top:1014px;width:566px;height:316px;border-radius:150px 140px 20px 20px;background:radial-gradient(ellipse at 50% 60%,#f15a2b 0%,#f15a2b 18%,#9ee7f2 19%,#8fe3ef 60%,#d8f6fa 100%)}

.art-callcenter{position:absolute;left:94px;top:1562px;width:430px;height:423px;border-radius:40px 120px 60px 160px;background:radial-gradient(ellipse at 50% 55%,#c9ecea 0%,#b7e5e3 60%,#dff3f2 100%)}
.service-call{left:599px;top:1584px;width:540px}
.check-columns{display:flex;gap:0}
.check-columns .check-list{width:266px}
.service-call .btn-cta{margin-top:49px}

/* footer */
.site-footer{position:absolute;left:0;top:2139px;width:1200px;height:220px;background:var(--footer);color:var(--footer-text);text-align:center}
.footer-contact{position:absolute;top:64px;left:0;width:100%;display:flex;justify-content:center;align-items:center;gap:22px;font-size:14.5px}
.footer-contact span{display:flex;align-items:center;gap:9px}
.footer-contact svg{width:14px;height:14px}
.footer-nav{position:absolute;top:106px;left:0;width:100%;display:flex;justify-content:center;gap:22px;font-size:14.5px}
.footer-nav a{color:var(--footer-text);text-decoration:none}
.sep{color:var(--footer-text)}
.copyright{position:absolute;top:146px;left:0;width:100%;font-size:14px}
</style>
</head>
<body>

<svg class="icons" aria-hidden="true">
  <defs>
    <symbol id="i-check" viewBox="0 0 16 16"><circle cx="8" cy="8" r="8" fill="#5cbd9a"/><path d="M4.4 8.3l2.4 2.4 4.8-5" fill="none" stroke="#fff" stroke-width="2" stroke-linecap="round" stroke-linejoin="round"/></symbol>
    <symbol id="i-mail" viewBox="0 0 16 12"><rect width="16" height="12" rx="1.5" fill="currentColor"/><path d="M1 1.5l7 5 7-5" fill="none" stroke="#fff" stroke-width="1.4"/></symbol>
    <symbol id="i-pin" viewBox="0 0 12 16"><path d="M6 0a6 6 0 016 6c0 4.5-6 10-6 10S0 10.5 0 6a6 6 0 016-6z" fill="currentColor"/><circle cx="6" cy="6" r="2.2" fill="#25272a"/></symbol>
    <symbol id="i-phone" viewBox="0 0 16 16"><path d="M3.3 0.6l2.4 3.1-1.5 2a9 9 0 006.1 6.1l2-1.5 3.1 2.4-1.4 2.7C8 15.3 .7 8 1.5 1.9z" fill="currentColor"/></symbol>
    <symbol id="i-search" viewBox="0 0 16 16"><circle cx="6.5" cy="6.5" r="5" fill="none" stroke="currentColor" stroke-width="2.4"/><path d="M10.3 10.3L15 15" stroke="currentColor" stroke-width="2.6" stroke-linecap="round"/></symbol>
    <symbol id="i-pencil" viewBox="0 0 16 16"><path d="M11.5 1l3.5 3.5L5.5 14 1 15l1-4.5z" fill="currentColor"/></symbol>
  </defs>
</svg>

<section class="hero">
  <div class="hero-photo" role="img" aria-label="Photo of a smiling man in a light grey suit talking on a corded desk phone in a bright office"></div>
  <h1 class="hero-title">LUMORA</h1>
  <p class="hero-lead">We are a call center that provides inbound and outbound calling &amp; marketing services for eCommerce store.</p>
  <div class="signup-form">
    <div class="signup-input"><svg style="color:#777"><use href="#i-mail"/></svg>Email Address</div>
    <div class="signup-btn">GET STARTED</div>
  </div>
</section>

<header class="site-header">
  <div class="brand"><span class="brand-mark"></span><span class="brand-name">LUMORA</span></div>
  <nav class="main-nav">
    <a class="is-active" href="#">HOME</a>
    <a href="#">ABOUT US</a>
    <a href="#">SERVICES</a>
    <a href="#">PRICING</a>
    <a href="#">CONTACT US</a>
    <svg class="nav-search" style="color:#333638"><use href="#i-search"/></svg>
  </nav>
  <a class="btn-signup" href="#"><svg><use href="#i-pencil"/></svg>SIGN UP</a>
</header>

<section class="welcome">
  <h2 class="section-title">WELCOME TO LUMORA</h2>
  <p class="welcome-text">Lumora is an omnichannel provider for customer care and back-end office support. We primarily work with eCommerce companies around the world. Our service is vital to the core operations and functionality of consumer-focused online eCommerce companies. Lumora originally started out as a generalized call center support company.</p>
</section>

<section class="service service-digital">
  <h2 class="section-title">DIGITAL SERVICES</h2>
  <p class="service-lead">Lumora is your personal customer service and product research team. We love eCommerce, but we love seeing business owners succeed even more!</p>
  <ul class="check-list">
    <li><svg><use href="#i-check"/></svg>Email Support</li>
    <li><svg><use href="#i-check"/></svg>Live Chat Support</li>
    <li><svg><use href="#i-check"/></svg>Product Research</li>
    <li><svg><use href="#i-check"/></svg>Product Listing</li>
    <li><svg><use href="#i-check"/></svg>Price Monitoring</li>
    <li><svg><use href="#i-check"/></svg>Product Photo &amp; Video Editing</li>
  </ul>
  <a class="btn-cta" href="#">GET STARTED</a>
</section>
<div class="art-digital" role="img" aria-label="Flat illustration of a laptop showing chat cards and messages over a light blue city skyline"></div>

<div class="art-callcenter" role="img" aria-label="Flat illustration of a support agent with a headset at a desk chatting with a customer, 24/7 service"></div>
<section class="service service-call">
  <h2 class="section-title">CALL CENTER SERVICES</h2>
  <p class="service-lead">Lumora is your personal customer service and product research team. We love eCommerce, but we love seeing business owners succeed even more!</p>
  <div class="check-columns">
    <ul class="check-list">
      <li><svg><use href="#i-check"/></svg>Answering service</li>
      <li><svg><use href="#i-check"/></svg>Welcome Calls</li>
      <li><svg><use href="#i-check"/></svg>Follow-Up Service</li>
      <li><svg><use href="#i-check"/></svg>Customer Upselling</li>
      <li><svg><use href="#i-check"/></svg>Over-The-Phone Order Taking</li>
      <li><svg><use href="#i-check"/></svg>Order Return Processing</li>
    </ul>
    <ul class="check-list">
      <li><svg><use href="#i-check"/></svg>Feedback/Survey Calls</li>
      <li><svg><use href="#i-check"/></svg>Message Delivering Service</li>
      <li><svg><use href="#i-check"/></svg>ROI Diagnostics &amp; Reporting</li>
      <li><svg><use href="#i-check"/></svg>Scalable Call Center Pricing</li>
      <li><svg><use href="#i-check"/></svg>Customizable For Any Industry</li>
      <li><svg><use href="#i-check"/></svg>100% US-Based Agents</li>
    </ul>
  </div>
  <a class="btn-cta" href="#">GET STARTED</a>
</section>

<footer class="site-footer">
  <div class="footer-contact">
    <span><svg><use href="#i-pin"/></svg>412 Harlow Ave. Brenton, CA 93790</span>
    <span class="sep">|</span>
    <span><svg><use href="#i-phone"/></svg>(800) 555-0147</span>
    <span class="sep">|</span>
    <span><svg><use href="#i-mail"/></svg>info@lumora.com</span>
  </div>
  <nav class="footer-nav">
    <a href="#">Home</a><span class="sep">|</span>
    <a href="#">About Us</a><span class="sep">|</span>
    <a href="#">Services</a><span class="sep">|</span>
    <a href="#">Pricing</a><span class="sep">|</span>
    <a href="#">Contact Us</a>
  </nav>
  <p class="copyright">Copyrights © 2018, Lumora. All rights reserved.</p>
</footer>

</body>
</html>
```